Business card and stationary design
Lindora Development
Business card and stationary design -
Creative Brief
Simple
Marike Holzner - van Brugt
MA, Cert. Coach & Advisor
Feldrainweg 14 6318 Seeried Switzerland
info@lindoradevelopment.ch
www.lindoradevelopment.ch
We're not sure about the font-type, could be the Logo-type or something that's compatible
Personal Coaching Health Coaching Business Coaching Consultancy out of the box, into the outdoors

```html
<!DOCTYPE html>
<html lang="en">
<head>
<meta charset="utf-8">
<title>Lindora Development – Stationery</title>
<link href="https://fonts.googleapis.com/css2?family=Open+Sans:wght@400;600&display=swap" rel="stylesheet">
<style>
  :root{
    --bg:#e9e6e1;
    --paper:#ffffff;
    --blue-deep:#1f3f9c;
    --blue-mid:#3a6fd0;
    --blue-light:#cfe0f7;
    --teal:#2f8f9a;
    --ink:#4a4f5c;
    --soft:#eef2f7;
    --shadow:rgba(40,30,20,.22);
  }
  *{box-sizing:border-box;margin:0;padding:0}
  html,body{width:1200px;height:619px;overflow:hidden}
  body{background:var(--bg);font-family:"Open Sans",sans-serif;color:var(--ink);position:relative}
  .sheet{position:absolute;background:var(--paper);box-shadow:2px 3px 8px var(--shadow);overflow:hidden}
  .band{position:absolute;left:0;right:0;top:0;background:linear-gradient(90deg,#ffffff 0%,var(--blue-light) 30%,var(--blue-mid) 70%,var(--blue-deep) 100%)}
  .brand{position:absolute;display:flex;flex-direction:column;align-items:center}
  .brand-dot{border-radius:50%;background:var(--paper);border:3px solid var(--teal)}
  .brand-name{color:var(--teal);font-weight:600;letter-spacing:.12em;line-height:1;white-space:nowrap}
  .contact{position:absolute;font-size:4.6px;line-height:1.7;color:var(--ink);white-space:nowrap}
  .contact span{display:block}
  .faint-mark{position:absolute;border-radius:50%;background:radial-gradient(circle at 40% 40%,#ffffff 0%,var(--soft) 70%,#e2e8f0 100%)}

  .letterhead{width:305px;height:432px;top:84px}
  .letterhead .band{height:30px}
  .letterhead .brand{left:18px;top:10px}
  .letterhead .brand-dot{width:38px;height:38px}
  .letterhead .brand-name{font-size:10px;margin-top:4px}
  .letterhead .contact{left:150px;top:36px}
  .letterhead .faint-mark{width:150px;height:150px;left:80px;top:250px}
  .lh-one{left:91px}
  .lh-two{left:451px}

  .envelope{left:792px;top:115px;width:312px;height:144px}
  .envelope .flap{position:absolute;left:0;top:0;width:100%;height:100%}
  .envelope .brand{left:128px;top:18px}
  .envelope .brand-dot{width:26px;height:26px;border-width:2px}
  .envelope .brand-name{font-size:7px;margin-top:3px}

  .slip{left:828px;top:211px;width:288px;height:173px}
  .slip .band{height:26px}
  .slip .brand{left:18px;top:10px}
  .slip .brand-dot{width:30px;height:30px;border-width:2px}
  .slip .brand-name{font-size:8px;margin-top:3px}
  .slip .contact{left:18px;top:78px}

  .card{width:216px;height:128px;top:372px;border-radius:3px}
  .card-front{left:703px}
  .card-front .band{height:20px}
  .card-front .brand{left:14px;top:8px}
  .card-front .brand-dot{width:34px;height:34px;border-width:3px}
  .card-front .brand-name{font-size:9px;margin-top:3px}
  .card-front .person{position:absolute;left:100px;top:28px;font-size:6px;font-weight:600;color:var(--ink);white-space:nowrap}
  .card-front .role{position:absolute;left:100px;top:37px;font-size:4.6px;white-space:nowrap}
  .card-front .contact{left:100px;top:52px}
  .card-front .foot{position:absolute;left:0;right:0;bottom:0;height:8px;background:linear-gradient(90deg,#ffffff,var(--blue-mid))}

  .card-back{left:929px;width:218px;height:132px}
  .card-back .brand-name{position:absolute;right:14px;top:14px;font-size:13px}
  .card-back .services{position:absolute;left:16px;top:58px;list-style:none;font-size:6px;line-height:1.9;color:var(--ink)}
  .card-back .services li{display:flex;align-items:center;gap:4px}
  .card-back .services svg{width:7px;height:7px}
  .card-back .foot{position:absolute;left:0;right:0;bottom:0;height:10px;background:linear-gradient(90deg,#ffffff,var(--blue-mid))}
</style>
</head>
<body>

<section class="sheet letterhead lh-one">
  <div class="band"></div>
  <div class="brand"><div class="brand-dot"></div><div class="brand-name">LINDORA</div></div>
  <div class="contact">
    <span>T +41 41 555 01 23</span>
    <span>M +41 79 555 04 56</span>
    <span>info@lindoradevelopment.ch</span>
    <span>www.lindoradevelopment.ch</span>
  </div>
  <div class="faint-mark" role="img" aria-label="Faint brand circle watermark"></div>
</section>

<section class="sheet letterhead lh-two">
  <div class="band"></div>
  <div class="brand"><div class="brand-dot"></div><div class="brand-name">LINDORA</div></div>
  <div class="contact">
    <span>Feldrainweg 14 6318</span>
    <span>Seeried Switzerland</span>
    <span>&nbsp;</span>
    <span>T +41 41 555 01 23</span>
    <span>M +41 79 555 04 56</span>
    <span>info@lindoradevelopment.ch</span>
    <span>www.lindoradevelopment.ch</span>
  </div>
  <div class="faint-mark" role="img" aria-label="Faint brand circle watermark"></div>
</section>

<section class="sheet envelope">
  <svg class="flap" viewBox="0 0 312 144" preserveAspectRatio="none">
    <polyline points="0,0 156,70 312,0" fill="none" stroke="#d9dde3" stroke-width="1"/>
  </svg>
  <div class="brand"><div class="brand-dot"></div><div class="brand-name">LINDORA</div></div>
</section>

<section class="sheet slip">
  <div class="band"></div>
  <div class="brand"><div class="brand-dot"></div><div class="brand-name">LINDORA</div></div>
  <div class="contact">
    <span>Feldrainweg 14 6318</span>
    <span>Seeried Switzerland</span>
  </div>
</section>

<section class="sheet card card-front">
  <div class="band"></div>
  <div class="brand"><div class="brand-dot"></div><div class="brand-name">LINDORA</div></div>
  <div class="person">Marike Holzner - van Brugt</div>
  <div class="role">MA, Cert. Coach &amp; Advisor</div>
  <div class="contact">
    <span>Feldrainweg 14 6318</span>
    <span>Seeried Switzerland</span>
    <span>T +41 41 555 01 23</span>
    <span>info@lindoradevelopment.ch</span>
    <span>www.lindoradevelopment.ch</span>
  </div>
  <div class="foot"></div>
</section>

<section class="sheet card card-back">
  <div class="brand-name">LINDORA</div>
  <ul class="services">
    <li><svg viewBox="0 0 8 8"><rect x=".5" y=".5" width="7" height="7" fill="none" stroke="#2f8f9a"/><path d="M2 4l1.5 1.5L6 2.5" fill="none" stroke="#2f8f9a"/></svg>Personal Coaching</li>
    <li><svg viewBox="0 0 8 8"><rect x=".5" y=".5" width="7" height="7" fill="none" stroke="#2f8f9a"/><path d="M2 4l1.5 1.5L6 2.5" fill="none" stroke="#2f8f9a"/></svg>Health Coaching</li>
    <li><svg viewBox="0 0 8 8"><rect x=".5" y=".5" width="7" height="7" fill="none" stroke="#2f8f9a"/><path d="M2 4l1.5 1.5L6 2.5" fill="none" stroke="#2f8f9a"/></svg>Business Coaching</li>
    <li><svg viewBox="0 0 8 8"><rect x=".5" y=".5" width="7" height="7" fill="none" stroke="#2f8f9a"/><path d="M2 4l1.5 1.5L6 2.5" fill="none" stroke="#2f8f9a"/></svg>Consultancy</li>
  </ul>
  <div class="foot"></div>
</section>

</body>
</html>
```